Personal Finance Author needs a postcard

Hi there,

I am a Canadian personal finance author and have published a new book called The Wealth Compass.

I teach Millennials how to create a 6-figure portfolio through investing (https://www.dariafelt.com/)

I'm speaking at some conferences so we were going to print some postcards to hand out to attendees with our info and calls-to-action on them.

I am looking for 4x6 (horizontal) postcard (no space needed for shipping label).

Logos, Headshots and Book Cover:
https://files.cloudvaultex.com/folders/8kQpZrT2mWvN4xLbJ7sHdYc3FgA9eUoRi?usp=sharing

Both sides will be full colour. I would like a clean and simple look. Our main sites are www.DariaFelt.com and www.TheWealthCompassBook.com if you want to get a sense of style and design.
I also uploaded a few marketing materials so you can see the existing designs.

Side 1:
Get Instant Access to your Free Resources - main headline

(small bullets underneath)
- The Wealth Compass Checklist
- Financial Worksheets
- Database of Investment Tools

DariaFelt.com/Resources

At the bottom, include "Don't forget to follow Daria Felt on social media:
Linkedin: @dariafelt7
Facebook: @thewealthcompassbook Instagram: @thewealthcompassbook Twitter: @WealthCompassBk"

Side 2:
Headline - Want to work directly with Daria and The Wealth Compass team to help you make your money grow and stay safe?

Work with us to (bullet point list)...
- Hire Daria as a Keynote Speaker
- Teach Financial Literacy Workshops
- Receive Financial Coaching

Want To Learn More About How We Can Help?
DariaFelt.com/Services

Include my contact info:
Daria Felt
Author | Speaker | Investor
daria@thewealthcompassbook.com
416-555-0187

Target Market(s)

Millennials who want to learn how to save and invest their money. I focus on stock market investing, real estate investing and entrepreneurship.

Industry/Entity Type

Financial Service

Font styles to use
Sans Serif

Colors

Designer to choose colors to be used in the design.

Requirements
Must have
• Photo of Daria Felt
• The Wealth Compass logo
• Green, Gold/Yellow to match existing colours
• modern business style postcard

```html
<!DOCTYPE html>
<html lang="en">
<head>
<meta charset="utf-8">
<title>The Wealth Compass – Postcard</title>
<link href="https://fonts.googleapis.com/css2?family=Archivo:ital,wght@0,600;0,800;1,700;1,800&family=Mulish:ital,wght@0,300;0,400;0,600;1,500;1,700&display=swap" rel="stylesheet">
<style>
  :root{
    --green:#12720a;
    --gold:#e8a70f;
    --gold-text:#f2b81d;
    --paper:#f2f2f2;
    --stage:#dcdcdc;
    --ink-green:#12720a;
    --social:#3b4fd6;
    --white:#ffffff;
  }
  *{margin:0;padding:0;box-sizing:border-box}
  html,body{width:1200px;height:1200px;overflow:hidden}
  body{background:var(--stage);position:relative;font-family:"Mulish",sans-serif}
  .postcard{position:absolute;left:240px;width:720px;height:480px;background:var(--paper);overflow:hidden;box-shadow:0 10px 24px rgba(0,0,0,.18)}
  .postcard--front{top:90px}
  .postcard--back{top:630px}
  .postcard__shapes{position:absolute;inset:0}
  .abs{position:absolute}

  /* front */
  .front__headline{left:50px;top:44px;font-family:"Archivo",sans-serif;font-style:italic;font-weight:800;font-size:28px;line-height:29px;color:var(--white);text-transform:uppercase}
  .front__photo{left:400px;top:18px;width:320px;height:462px;background:linear-gradient(180deg,#e9e6e3 0%,#c99a82 30%,#e6e3e0 55%,#8e9a96 75%,#7f8b87 100%);border-radius:150px 150px 0 0}
  .front__nametag{left:558px;top:432px;padding:3px 9px;border-radius:12px;background:rgba(18,114,10,.35);color:var(--white);font-size:11px;letter-spacing:.8px}
  .resource-list{left:45px;top:223px;list-style:none;font-size:13px;line-height:16px;color:var(--ink-green);font-weight:400}
  .resource-list li{display:flex;align-items:center;gap:6px}
  .resource-list svg{width:16px;height:10px}
  .visit-pill{left:117px;top:292px;width:75px;height:15px;border-radius:8px;background:var(--gold);color:var(--white);font-size:10px;line-height:15px;text-align:center;letter-spacing:.6px}
  .front__url{left:63px;top:308px;font-size:15px;font-style:italic;font-weight:500;color:var(--ink-green)}
  .brand-name{left:40px;top:360px;width:125px;font-family:"Archivo",sans-serif;font-weight:800;color:var(--ink-green);text-transform:uppercase;text-align:center;line-height:1}
  .brand-name span{display:block}
  .brand-name .l1{font-size:15px}
  .brand-name .l2{font-size:29px}
  .brand-name .l3{font-size:25px}
  .social{left:187px;top:369px;color:var(--ink-green)}
  .social__title{font-size:12.5px;line-height:13px;font-style:italic;font-weight:700}
  .social__rule{width:28px;height:3px;background:var(--gold);margin:4px 0 6px}
  .social__list{list-style:none;font-size:7px;line-height:13px;color:#333}
  .social__list li{display:flex;align-items:center;gap:4px}
  .social__dot{width:9px;height:9px;border-radius:50%;background:var(--social)}

  /* back */
  .back__headline{left:46px;top:42px;width:340px;font-family:"Archivo",sans-serif;font-style:italic;font-weight:800;font-size:19.5px;line-height:23px;color:var(--white)}
  .back__headline em{color:var(--gold-text)}
  .services__title{left:46px;top:210px;font-family:"Archivo",sans-serif;font-style:italic;font-weight:800;font-size:19.5px;color:var(--white)}
  .services__rule{left:46px;top:233px;width:54px;height:3px;background:var(--white)}
  .services__list{left:46px;top:240px;list-style:none;color:var(--gold-text);font-size:10px}
  .services__list li{display:flex;align-items:center;gap:7px;height:21.5px}
  .services__icon{width:18px;height:18px;border-radius:50%;background:var(--gold);display:flex;align-items:center;justify-content:center}
  .contact{left:46px;top:364px;color:var(--white)}
  .contact__name,.contact__role{font-size:16.5px;line-height:21px;font-weight:400;letter-spacing:.3px}
  .contact__detail{font-size:14px;line-height:18px;font-weight:300;letter-spacing:.4px;opacity:.9}
  .back__book{left:440px;top:38px;width:250px;height:362px;background:linear-gradient(160deg,#f4f4f0 0%,#dfe4da 45%,#2f7a28 80%,#1c5e17 100%);border-radius:4px}
  .back__cta{left:400px;top:422px;width:300px;text-align:center;font-size:13px;font-style:italic;font-weight:600;color:var(--ink-green)}
  .back__pill{left:469px;top:443px;width:162px;height:19px;border-radius:10px;background:var(--gold);color:var(--white);font-size:11px;line-height:19px;text-align:center}
</style>
</head>
<body>

<section class="postcard postcard--front">
  <svg class="postcard__shapes" viewBox="0 0 720 480" aria-hidden="true">
    <path d="M0 0 H440 C400 90 300 175 150 175 C90 175 40 171 0 168 Z" fill="var(--green)"/>
    <path d="M440 0 H472 C435 110 335 185 175 178 C320 163 410 90 440 0 Z" fill="var(--gold)"/>
  </svg>
  <div class="abs front__photo" role="img" aria-label="Portrait photo of Daria Felt in a grey blazer"></div>
  <div class="abs front__nametag">DARIA FELT</div>

  <h1 class="abs front__headline">Get instant<br>access to your<br>free resources</h1>

  <ul class="abs resource-list">
    <li><svg viewBox="0 0 16 10"><path d="M1 6 L5 9 L15 1" fill="none" stroke="var(--gold)" stroke-width="2.4" stroke-linecap="round" stroke-linejoin="round"/></svg>The Wealth Compass Checklist</li>
    <li><svg viewBox="0 0 16 10"><path d="M1 6 L5 9 L15 1" fill="none" stroke="var(--gold)" stroke-width="2.4" stroke-linecap="round" stroke-linejoin="round"/></svg>Financial Worksheets</li>
    <li><svg viewBox="0 0 16 10"><path d="M1 6 L5 9 L15 1" fill="none" stroke="var(--gold)" stroke-width="2.4" stroke-linecap="round" stroke-linejoin="round"/></svg>Database of Investment Tools</li>
  </ul>

  <div class="abs visit-pill">VISIT AT</div>
  <div class="abs front__url">DariaFelt.com/Resources</div>

  <div class="abs brand-name"><span class="l1">The</span><span class="l2">Wealth</span><span class="l3">Compass</span></div>

  <div class="abs social">
    <p class="social__title">Follow Daria Felt<br>on social media</p>
    <div class="social__rule"></div>
    <ul class="social__list">
      <li><span class="social__dot"></span>@dariafelt7</li>
      <li><span class="social__dot"></span>@WealthCompassBk</li>
      <li><span class="social__dot"></span>@thewealthcompassbook</li>
      <li><span class="social__dot"></span>@thewealthcompassbook</li>
    </ul>
  </div>
</section>

<section class="postcard postcard--back">
  <svg class="postcard__shapes" viewBox="0 0 720 480" aria-hidden="true">
    <path d="M0 0 H414 C422 160 398 340 248 480 H0 Z" fill="var(--green)"/>
    <path d="M420 140 C430 300 385 405 296 480 H266 C372 400 418 300 420 140 Z" fill="var(--gold)"/>
  </svg>

  <h2 class="abs back__headline">Want to work directly with Daria and The Wealth Compass team to help you make your <em>MONEY GROW</em> and <em>STAY SAFE</em>?</h2>

  <h3 class="abs services__title">WORK WITH US TO:</h3>
  <div class="abs services__rule"></div>
  <ul class="abs services__list">
    <li><span class="services__icon"><svg width="10" height="10" viewBox="0 0 10 10"><circle cx="5" cy="2.5" r="2" fill="var(--green)"/><path d="M1.5 10 V7 Q5 4 8.5 7 V10 Z" fill="var(--green)"/></svg></span>Hire Daria as a Keynote Speaker</li>
    <li><span class="services__icon"><svg width="10" height="10" viewBox="0 0 10 10"><rect x="1" y="1.5" width="8" height="5.5" fill="none" stroke="var(--green)" stroke-width="1.3"/><path d="M5 7 V9.5 M3 9.5 H7" stroke="var(--green)" stroke-width="1.3"/></svg></span>Teach Financial Literacy Workshops</li>
    <li><span class="services__icon"><svg width="10" height="10" viewBox="0 0 10 10"><circle cx="5" cy="2.5" r="1.6" fill="var(--green)"/><circle cx="2.2" cy="7" r="1.4" fill="var(--green)"/><circle cx="7.8" cy="7" r="1.4" fill="var(--green)"/></svg></span>Receive Financial Coaching</li>
  </ul>

  <div class="abs contact">
    <p class="contact__name">Daria Felt</p>
    <p class="contact__role">Author | Speaker | Investor</p>
    <p class="contact__detail">416-555-0187</p>
    <p class="contact__detail">daria@thewealthcompassbook.com</p>
  </div>

  <div class="abs back__book" role="img" aria-label="Stack of The Wealth Compass books by Daria Felt"></div>
  <p class="abs back__cta">Want To Learn More About How We Can Help?</p>
  <div class="abs back__pill">DariaFelt.com/Resources</div>
</section>

</body>
</html>
```